Create Premium Wine Label Design

We are premium wine exporters from Australia. We are looking to introduce new brand " The Velloro" - in red wine, White wine and Sparkling wine to international market.

The sample label design for red wine ( Shiraz) is attached.

This is our luxury brand. We need a stunning wine label designs for (front, back and neck) that should be mostly in GOLD colour and design should be really eye catching.

We have provided sample design for front, back and neck labels. However, we are looking forward to see a completely new improvised design.

LOGO attached.

Front Label Design Specification:

* We would like to see designs that are in Gold colour.
* Wine Bottle size is standard: 750ml; we assume the same design can be resizable to different bottle sizes.
* Our design should suit both black, white and sparkling wine bottles(sample attached)
* Use our logo in the design (see attached - label sample)
* Content for front label (see attached).
* Design should include all information specified in the sample

Back Label Design
* All contents in the sample should be used ( sample attached)
* LOGO attached.

Neck Label Design
* Sample of Neck label attached, please provide similar or your own design.
* LOGO attached.

Image Samples:
* Samples of label designs we like (see attached)
* Sample for gold color (see attached)
* For bottle shapes (see attached)
* Front, Back and Neck Label Samples (see attached)

Target Market(s)

International Wine Market

Font styles to use
Decorative
Script

Requirements
Must have
• Must have golden color on front and back label

```html
<!DOCTYPE html>
<html lang="en">
<head>
<meta charset="utf-8">
<title>The Velloro Shiraz – Label Set</title>
<link rel="stylesheet" href="https://fonts.googleapis.com/css2?family=Arimo:wght@400;500&family=Cinzel:wght@400;600&family=Crimson+Text:wght@400;600&family=Uncial+Antiqua&display=swap">
<style>
  :root {
    --backdrop: #f1efeb;
    --label-black: #0d0c0b;
    --label-black-soft: #1c1a17;
    --label-white: #fdfcf9;
    --gold: #c9a24a;
    --gold-light: #f1d98a;
    --gold-deep: #9a7425;
    --gold-faint: #efe3c4;
    --ink: #2b2824;
    --cream-text: #f4f1ea;
  }
  * { box-sizing: border-box; margin: 0; padding: 0; }
  html, body {
    width: 1200px; height: 1200px; overflow: hidden;
    background: var(--backdrop);
  }
  .canvas { position: relative; width: 1200px; height: 1200px; }

  /* ---------- Back label ---------- */
  .back-label {
    position: absolute; left: 50px; top: 320px;
    width: 520px; height: 452px;
    background: var(--label-white);
    box-shadow: 0 4px 18px rgba(0,0,0,.12);
    overflow: hidden;
    color: var(--ink);
    font-family: "Crimson Text", Georgia, serif;
    text-align: center;
  }
  .back-label .pattern-field {
    position: absolute; left: 0; right: 0; top: 240px; bottom: 0;
    background: linear-gradient(180deg, rgba(239,227,196,0) 0%, var(--gold-faint) 45%, #e8d7ab 100%);
  }
  .back-label .content { position: relative; padding: 22px 22px 0; }
  .back-label .brand-name {
    font-family: "Cinzel", Georgia, serif; font-weight: 600;
    font-size: 24px; letter-spacing: 3px; color: var(--gold-deep);
    display: inline-flex; align-items: center; gap: 10px;
  }
  .brand-dot {
    width: 10px; height: 10px; border-radius: 50%; background: currentColor;
  }
  .back-label .varietal { font-size: 30px; margin-top: 18px; line-height: 1; }
  .back-label .wine-name { font-family: "Arimo", Arial, sans-serif; font-size: 16px; margin-top: 6px; }
  .back-label .tasting-note {
    font-size: 12.6px; line-height: 1.42; text-align: justify; margin-top: 4px;
  }
  .back-label .origin { font-family: "Arimo", Arial, sans-serif; font-size: 16px; margin-top: 10px; }
  .back-label .details, .back-label .producer {
    font-family: "Arimo", Arial, sans-serif; font-size: 11.5px; line-height: 1.55; margin-top: 6px;
  }
  .back-label .producer { margin-top: 18px; }

  /* ---------- Front label ---------- */
  .front-label {
    position: absolute; left: 610px; top: 242px;
    width: 540px; height: 616px;
    background: radial-gradient(ellipse at 50% 30%, var(--label-black-soft) 0%, var(--label-black) 70%);
    box-shadow: 0 6px 22px rgba(0,0,0,.25);
    overflow: hidden;
    text-align: center;
  }
  .front-label .gold-rule {
    position: absolute; left: 0; right: 0; height: 2px;
    background: linear-gradient(90deg, var(--gold-deep), var(--gold-light), var(--gold-deep));
  }
  .front-label .rule-top { top: 14px; height: 3px; }
  .front-label .rule-bottom-a { top: 558px; }
  .front-label .rule-bottom-b { top: 564px; height: 1px; }
  .front-label .pattern-field {
    position: absolute; left: 0; right: 0; top: 360px; height: 198px;
    background: linear-gradient(180deg, rgba(154,116,37,0) 0%, rgba(154,116,37,.28) 40%, rgba(201,162,74,.42) 100%);
  }
  .front-label .brand-name {
    position: absolute; left: 0; right: 0; top: 78px;
    font-family: "Cinzel", Georgia, serif; font-weight: 600;
    font-size: 32px; letter-spacing: 4px; color: var(--gold);
    display: flex; justify-content: center; align-items: center; gap: 12px;
  }
  .front-label .brand-underline {
    position: absolute; left: 200px; width: 140px; top: 136px; height: 1px;
    background: var(--gold);
  }
  .front-label .wine-name {
    position: absolute; left: 0; right: 0; top: 196px;
    font-family: "Arimo", Arial, sans-serif; font-size: 56px; line-height: 1;
    background: linear-gradient(180deg, var(--gold-light) 0%, var(--gold) 55%, var(--gold-deep) 100%);
    -webkit-background-clip: text; background-clip: text; color: transparent;
  }
  .front-label .varietal {
    position: absolute; left: 0; right: 0; top: 270px;
    font-family: "Uncial Antiqua", "Times New Roman", serif;
    font-size: 74px; line-height: 1; color: var(--cream-text);
  }
  .front-label .vintage {
    position: absolute; left: 0; right: 0; top: 360px;
    font-family: "Cinzel", Georgia, serif; font-size: 22px; letter-spacing: 6px;
    color: var(--cream-text);
  }
  .front-label .appellation {
    position: absolute; left: 0; right: 0; top: 522px;
    font-family: "Arimo", Arial, sans-serif; font-size: 22px; color: var(--gold);
  }
  .front-label .volume, .front-label .strength {
    position: absolute; top: 576px;
    font-family: "Crimson Text", Georgia, serif; font-size: 19px; color: #cdb98a;
  }
  .front-label .volume { left: 22px; }
  .front-label .strength { right: 22px; }
</style>
</head>
<body>
<main class="canvas">

  <section class="back-label" aria-label="Back label">
    <div class="pattern-field" role="img" aria-label="Fine gold diamond line pattern"></div>
    <div class="content">
      <div class="brand-name"><span class="brand-dot"></span>CORVALLA</div>
      <h2 class="varietal">Shiraz</h2>
      <p class="wine-name">The Velloro</p>
      <p class="tasting-note">Australian Shiraz The Velloro is a classic fruit driven wine bursting with aromas of dark fruits and spice with background notes of charred French oak. This is a full bodied wine showcasing rich and juicy dark fruits of plum and cherry balanced with soft tannins and oak, providing a long lasting finish. This wine matches perfectly with a range of rich and hearty red meat or pasta.</p>
      <p class="origin">Product of Australia</p>
      <p class="details">Preservative (220) Antioxidant (300)<br>May Contain Traces of Milk<br>Country of Origin: Australia</p>
      <p class="producer">Corvalla Wines Pty. Ltd.<br>Melbourne,<br>Victoria, Australia</p>
    </div>
  </section>

  <section class="front-label" aria-label="Front label">
    <div class="pattern-field" role="img" aria-label="Gold art deco diamond line pattern"></div>
    <div class="gold-rule rule-top"></div>
    <div class="brand-name"><span class="brand-dot"></span>CORVALLA</div>
    <div class="brand-underline"></div>
    <h1 class="wine-name">The Velloro</h1>
    <p class="varietal">Shiraz</p>
    <p class="vintage">2018</p>
    <p class="appellation">Wine of Australia</p>
    <div class="gold-rule rule-bottom-a"></div>
    <div class="gold-rule rule-bottom-b"></div>
    <span class="volume">750 Ml.</span>
    <span class="strength">Alc. 12.5 By Volume</span>
  </section>

</main>
</body>
</html>
```